Website for New Phone Company

Our company "Lagoonway Telecom" requires a new web-site.

We enable Pacific Islanders (Fijians, Samoans, Tongans) to speak to their friends and family back home for a fraction of the cost of other phone companies whilst maintaining a quality. Our target audience is price sensitive but is demanding with quality, we would like them to gather a feel that they are dealing with a safe company that is orientated towards the Pacific Island community, has low pricing and yet doesn't compromise on quality.

We are going to be marketing via online channels and so a Google friendly web-site is important. We essentially need three pages designed which we will use with our content.

Page 1 - Homepage Lagoonway Telecom - Our prime brand is Lagoonway Telecom and we would like to promote this brand on our web-site.

However, we have three plans under this brand called Verelo, Makiri and Nemali. We would like the main page to have three unique service offerings for Nemali, Makiri and Verelo. Something along the lines of being able to choose a plan down on the page. I would like to give examples here of companies in our industry that are extremely successful in this trade i.e. www.dialquay.co.nz, www.9speak.co.nz, www.telvira.com

The objective of this design is to present the customer with three unique offerings targeted to Samoa (Nemali), Makiri (Tonga) and Verelo (Fiji).

Page 2 - Content/Template Page for Lagoonway Telecom - We require a page where we can place content like About Us, Contact Us etc.

Page 3 - We require a single design that will fit all three brands as per the brand images attached for Verelo, Nemali and Makiri. This will almost be used as a landing page to brand the plan exclusively under our company. All three plans / service offerings are being marketed under "Lagoonway Telecom" which makes it important to use both the service offering logo as well as the company logo. This page needs to act more as a promotional page where it promotes our service offering. e.g. Call Samoa from only 50c a minute type of thing.

The objective of the design of the landing / service offering page is to entice the customer to act upon the offer by joining our organisation.

We will be available throughout the process to guide you better.
Updates

Project Deadline Extended
Reason: We haven't received suitable designs to choose from. We would like to see quality work not quantity.

Industry/Entity Type

It Company

```html
<!DOCTYPE html>
<html lang="en">
<head>
<meta charset="utf-8">
<title>Lagoonway Telecom</title>
<link rel="stylesheet" href="https://fonts.googleapis.com/css2?family=Arimo:wght@400;700&family=Oswald:wght@300;400;500&display=swap">
<style>
  :root{
    --brand-red:#d7201b;
    --brand-grey:#7a7a7a;
    --ink:#2b2b2b;
    --muted:#a9a9a9;
    --rule:#d6d6d6;
    --footer-bg:#f0f0f0;
    --sky:#3f8fd6;
    --sea:#2fb3c2;
    --sand:#ece9e2;
    --verelo:#c4562a;
    --nemali:#c8c83a;
    --makiri:#8cc63f;
    --btn-top:#ee5a51;
    --btn-bottom:#d4231c;
  }
  *{box-sizing:border-box;margin:0;padding:0}
  html,body{width:1200px;height:1144px;overflow:hidden;background:#fff}
  .page{position:relative;width:1200px;height:1144px;overflow:hidden;font-family:"Arimo",Arial,sans-serif}

  .site-header{position:absolute;left:0;top:0;width:1200px;height:114px;border-top:3px solid var(--brand-red);border-bottom:3px solid #e4e4e4;background:#fff}
  .brand{position:absolute;left:82px;top:22px;display:flex;align-items:center;gap:16px}
  .brand-dot{width:62px;height:62px;border-radius:50%;background:var(--brand-red)}
  .brand-name{font-family:"Arimo",Arial,sans-serif;font-weight:700;font-size:36px;color:var(--brand-grey);letter-spacing:-0.5px}

  .social{position:absolute;top:22px;right:76px;display:flex;align-items:center;gap:28px;font-size:12px;color:#555}
  .social-item{display:flex;align-items:center;gap:6px}
  .social-square{width:19px;height:19px;background:#4a86c5}
  .social-square.plus{width:54px;background:#fff;border:1px solid #cfcfcf}

  .main-nav{position:absolute;right:64px;top:74px;display:flex;gap:8px}
  .main-nav a{display:block;padding:5px 10px;font-size:13px;color:#222;text-decoration:none;letter-spacing:.2px;border-radius:4px}
  .main-nav a.is-active{background:var(--brand-red);color:#fff;font-weight:700}

  .hero{position:absolute;left:0;top:114px;width:1200px;height:412px;
    background:linear-gradient(180deg,var(--sky) 0%,#8cc2ea 36%,#d9ecf7 48%,var(--sea) 53%,#5cc4c8 62%,var(--sand) 66%,#f3f1ec 100%)}

  .plans{position:absolute;left:42px;top:561px;width:1113px;display:flex;justify-content:space-between}
  .plan-card{width:348px;height:485px;border:1px solid var(--rule);background:#fff;text-align:center;position:relative;font-family:"Oswald","Arial Narrow",sans-serif}
  .plan-mark{width:72px;height:72px;border-radius:50%;margin:30px auto 0}
  .plan-name{margin-top:14px;font-family:"Oswald","Arial Narrow",sans-serif;font-weight:400;font-size:44px;line-height:50px;letter-spacing:1px}
  .plan-card.verelo .plan-mark{background:var(--verelo)} .plan-card.verelo .plan-name{color:var(--verelo)}
  .plan-card.nemali .plan-mark{background:#f2c31b} .plan-card.nemali .plan-name{color:var(--nemali)}
  .plan-card.makiri .plan-mark{background:var(--makiri)} .plan-card.makiri .plan-name{color:var(--makiri)}
  .plan-validity{margin-top:18px;font-weight:300;font-size:27px;color:var(--muted)}
  .plan-price{margin-top:2px;font-weight:500;font-size:60px;line-height:70px;color:var(--ink)}
  .plan-period{font-weight:300;font-size:27px;color:var(--muted)}
  .buy-button{position:absolute;left:41px;top:355px;width:264px;height:58px;border-radius:4px;border:1px solid #c81e18;
    background:linear-gradient(180deg,var(--btn-top),var(--btn-bottom));color:#fff;font-size:30px;line-height:56px;font-weight:400;text-decoration:none}
  .read-more{position:absolute;left:0;right:0;top:434px;font-size:27px;color:var(--ink);font-weight:400}

  .site-footer{position:absolute;left:0;top:1090px;width:1200px;height:54px;background:var(--footer-bg);border-top:2px solid #e2e2e2;font-size:10.5px;color:#333}
  .copyright{position:absolute;left:40px;top:22px}
  .copyright span{color:var(--brand-red)}
</style>
</head>
<body>
<div class="page">
  <header class="site-header">
    <div class="brand">
      <div class="brand-dot"></div>
      <div class="brand-name">Lagoonway Telecom</div>
    </div>
    <div class="social">
      <div class="social-item"><span class="social-square plus"></span></div>
      <div class="social-item"><span class="social-square"></span>Join us</div>
      <div class="social-item"><span class="social-square" style="background:#41a9dd"></span>Follow us</div>
    </div>
    <nav class="main-nav">
      <a href="#" class="is-active">HOME</a>
      <a href="#">PHONECARDS</a>
      <a href="#">RECHARGE</a>
      <a href="#">PRODUCTS</a>
      <a href="#">ABOUT US</a>
      <a href="#">CONTACT</a>
    </nav>
  </header>

  <div class="hero" role="img" aria-label="Photo of a couple holding hands on a white sand beach under a palm tree, facing a turquoise sea and blue sky"></div>

  <section class="plans">
    <article class="plan-card verelo">
      <div class="plan-mark"></div>
      <h2 class="plan-name">Verelo</h2>
      <p class="plan-validity">valid for 1 year</p>
      <p class="plan-price">$7.79</p>
      <p class="plan-period">per month</p>
      <a href="#" class="buy-button">Buy Now</a>
      <a href="#" class="read-more" style="text-decoration:none">read more</a>
    </article>
    <article class="plan-card nemali">
      <div class="plan-mark"></div>
      <h2 class="plan-name">Nemali</h2>
      <p class="plan-validity">valid for 1 year</p>
      <p class="plan-price">$9.79</p>
      <p class="plan-period">per month</p>
      <a href="#" class="buy-button">Buy Now</a>
      <a href="#" class="read-more" style="text-decoration:none">read more</a>
    </article>
    <article class="plan-card makiri">
      <div class="plan-mark"></div>
      <h2 class="plan-name">Makiri</h2>
      <p class="plan-validity">valid for 1 year</p>
      <p class="plan-price">$11.79</p>
      <p class="plan-period">per month</p>
      <a href="#" class="buy-button">Buy Now</a>
      <a href="#" class="read-more" style="text-decoration:none">read more</a>
    </article>
  </section>

  <footer class="site-footer">
    <p class="copyright">Copyright 2014 <span>Lagoonway Telecom</span>, All rights reserved.</p>
  </footer>
</div>
</body>
</html>
```